Cutting edge GUI for a conventional C# Forms Project

I have an existing C# Forms application. The current GUI design format is Win 95 style forms. I would like to elevate the look of the software.

There are a total of six forms. Apart from two forms at 1024 X 600, the others are of different sizes. I am open to resizing them depending on the design.

I am attaching the user manual of the product to give you a better idea of what the application does. The manual also contains screenshots of individual screens. I am open to sharing the C# source files if needed.

Target Market(s)

Industrial application - Field Representatives - Will be used in Outdoor environments.

Industry/Entity Type

Software

Requirements
Must have
• A very cool, futuristic design.
Design should be light-weight as the application maybe run on net-books and low end tablets.
Should not have
• Redundant point but keep in mind that this design is going to be used in a software. So light weight is highly appreciated.

```html
<!DOCTYPE html>
<html lang="en">
<head>
<meta charset="utf-8">
<title>ViewRuns</title>
<link rel="stylesheet" href="https://fonts.googleapis.com/css2?family=Pathway+Gothic+One&family=Roboto:wght@400&display=swap">
<style>
:root{
  --titlebar:#3a3a3a;
  --brand:#1f9a4a;
  --panel-top:#7b7b7b;
  --panel-bottom:#636363;
  --light-panel:#f4f4f4;
  --accent-blue:#35b4ec;
  --accent-yellow:#f5ee7a;
  --header-red:#b03232;
  --row:#565656;
  --row-line:#8a8a8a;
  --progress:#2a7f55;
  --button:#c9c9c9;
  --ink:#111;
  --white:#fff;
}
*{box-sizing:border-box;margin:0;padding:0}
html,body{width:1200px;height:675px;overflow:hidden}
body{font-family:"Pathway Gothic One",sans-serif;color:var(--white);
  background:linear-gradient(#f2f2f2 0,#dcdcdc 230px,#9a9a9a 420px,#7c7c7c 675px);position:relative}
.abs{position:absolute}
.titlebar{left:0;top:0;width:1200px;height:31px;background:linear-gradient(#4a4a4a,#2f2f2f);display:flex;align-items:center}
.brand-mark{width:20px;height:20px;background:var(--brand);margin-left:6px}
.app-name{font-family:"Roboto",sans-serif;font-size:19px;margin-left:9px}
.window-controls{position:absolute;right:4px;top:4px;display:flex;gap:3px}
.window-controls span{width:22px;height:22px;background:var(--white);display:block}
.panel{background:linear-gradient(var(--panel-top),var(--panel-bottom));text-align:center;font-size:17px}
.panel .label{color:var(--accent-blue);font-size:21px;display:block}
.back{background:var(--light-panel);color:var(--ink);font-size:20px;display:flex;align-items:center;justify-content:center}
.time-box{padding-top:8px;line-height:1.3}
.status{left:430px;top:40px;width:330px;text-align:center;color:var(--ink)}
.status h1{font-size:56px;font-weight:400;letter-spacing:1px;line-height:1}
.status p{font-size:21px;margin-top:74px}
.spinner{left:563px;top:110px}
.details-tab{left:773px;top:37px;width:42px;height:183px;background:var(--accent-yellow);color:var(--ink);font-size:27px;display:flex;align-items:center;justify-content:center}
.details-tab span{transform:rotate(-90deg);white-space:nowrap;letter-spacing:1px}
.info{padding-top:9px;line-height:1.35}
.info .label{margin-bottom:6px}
table{left:12px;top:237px;width:1129px;border-collapse:collapse;font-size:18px;table-layout:fixed}
th{background:var(--header-red);height:52px;font-weight:400;font-size:20px;border-right:1px solid #d06a6a}
th:last-child{border-right:0}
tbody tr:first-child td{border-top:6px solid #9a9a9a}
td{height:34.5px;text-align:center;background:linear-gradient(#616161,#4d4d4d);border:1px solid var(--row-line);border-left:0}
td:last-child{border-right:0}
td.done{background:var(--progress)}
.scrollbar{left:1146px;top:237px;width:42px;height:368px;background:linear-gradient(#6e6e6e,#474747)}
.button{top:618px;width:225px;height:50px;background:var(--button);color:var(--ink);font-size:21px;display:flex;align-items:center;justify-content:center}
.units{left:964px;top:618px;width:225px;height:50px;background:#3d3d3d;display:flex;align-items:center;justify-content:center;gap:10px;font-size:21px}
.radio{width:15px;height:15px;border-radius:50%;background:var(--white);display:inline-block;vertical-align:-2px;margin-right:6px}
.radio.on{background:#1e88e5;border:2px solid var(--white)}
</style>
</head>
<body>
<header class="abs titlebar">
  <div class="brand-mark"></div>
  <div class="app-name">ViewRuns</div>
  <div class="window-controls"><span></span><span></span><span></span></div>
</header>

<div class="abs back" style="left:12px;top:35px;width:225px;height:54px">Back to main menu</div>
<div class="abs panel time-box" style="left:12px;top:91px;width:225px;height:63px"><span class="label">Tool ON Time</span>July 8 2012 &nbsp;&nbsp; 03:21:17</div>
<div class="abs panel time-box" style="left:12px;top:159px;width:225px;height:63px"><span class="label">Download Time</span>July 8, 2012 &nbsp;&nbsp; 03:21:39</div>
<div class="abs panel" style="left:242px;top:35px;width:182px;height:186px"></div>

<section class="abs status">
  <h1>DOWNLOADING...</h1>
  <p>2 RECORDS TO DOWNLOAD</p>
</section>
<svg class="abs spinner" width="64" height="64" viewBox="0 0 64 64" aria-hidden="true">
  <circle cx="32" cy="32" r="29" fill="none" stroke="#fff" stroke-width="3"/>
  <circle cx="32" cy="32" r="29" fill="none" stroke="#222" stroke-width="3" stroke-dasharray="60 122"/>
  <circle cx="32" cy="32" r="22" fill="#fff"/>
  <path d="M20 36 A13 13 0 1 1 40 42" fill="none" stroke="#111" stroke-width="4"/>
</svg>

<div class="abs details-tab"><span>DETAILS</span></div>
<div class="abs panel info" style="left:820px;top:35px;width:182px;height:90px"><span class="label">Job Number</span>CetB00103</div>
<div class="abs panel info" style="left:1007px;top:35px;width:182px;height:90px"><span class="label">Distance</span>0.73 Feet<br>0.00 Mile</div>
<div class="abs panel info" style="left:820px;top:131px;width:182px;height:90px"><span class="label">Run Type</span>Frequency<br>1065 Samples per second</div>
<div class="abs panel info" style="left:1007px;top:131px;width:182px;height:90px"><span class="label">Tool Size</span>6 inch</div>

<table class="abs">
  <colgroup><col style="width:85px"><col style="width:216px"><col style="width:165px"><col style="width:166px"><col style="width:164px"><col style="width:165px"><col style="width:168px"></colgroup>
  <thead><tr><th>S.No</th><th>Time</th><th>Distance (Ft)</th><th>Min ID (In)</th><th>O 'Clock</th><th>Length (In)</th><th>Progress</th></tr></thead>
  <tbody>
    <tr><td>1</td><td>July 8, 2012 &nbsp;&nbsp; 03:21:20</td><td>0</td><td></td><td></td><td></td><td class="done">50 %</td></tr>
    <tr><td>2</td><td>July 8, 2012 &nbsp;&nbsp; 03:21:26</td><td>0.73</td><td></td><td></td><td></td><td>0 %</td></tr>
    <tr><td>3</td><td>July 8, 2012 &nbsp;&nbsp; 03:21:30</td><td>0.73</td><td>5.04</td><td>03:28</td><td>0</td><td class="done">100 %</td></tr>
    <tr><td>4</td><td>July 8, 2012 &nbsp;&nbsp; 03:21:32</td><td>0.73</td><td>5.07</td><td>09:12</td><td>0</td><td class="done">100 %</td></tr>
    <tr><td></td><td></td><td></td><td></td><td></td><td></td><td></td></tr>
    <tr><td></td><td></td><td></td><td></td><td></td><td></td><td></td></tr>
    <tr><td></td><td></td><td></td><td></td><td></td><td></td><td></td></tr>
    <tr><td></td><td></td><td></td><td></td><td></td><td></td><td></td></tr>
    <tr><td></td><td></td><td></td><td></td><td></td><td></td><td></td></tr>
  </tbody>
</table>
<div class="abs scrollbar"></div>

<div class="abs button" style="left:12px">Previous Run</div>
<div class="abs button" style="left:250px">Next Run</div>
<div class="abs button" style="left:608px">Create Report</div>
<div class="abs units"><span><i class="radio on"></i>Imperial</span><span><i class="radio"></i>Metric</span></div>
</body>
</html>
```